Coral drift hour Banner promoting freedom and adventure working from laptop

I need 3 different banners in 4 different sizes
I am an online business working from home on my laptop. I am in the motivational program and internet marketing industry and would like some banners that reflect healthy, fun and financially free lifestyle.
I have a Chatterly page title of UpWithSun and a website called Coraldrifthour.com
I have uploaded some photos but am unsure what may be required for the banners.
I am on the Gold Coast Australia but will be advertising in America, UK, Canada etc.

Target Market(s)

Adventure and Health fitness

Colors

Designer to choose colors to be used in the design.

Requirements
Must have
• Promotion of a living a financially free life through the ability of working from home via your own online business.
• Fun fit healthy freedom and adventure associated with someone living their dream life from working from home away from the 9 to 5 hustle and bussle.
Nice to have
• beaches, mountains and working from a Zentra slate air.
• Showing fun and adventure from someone living this lifestyle.

```html
<!DOCTYPE html>
<html lang="en">
<head>
<meta charset="utf-8">
<title>Coral drift hour – Work from Home banner</title>
<link rel="stylesheet" href="https://fonts.googleapis.com/css2?family=Delius&family=Varela+Round&display=swap">
<style>
  :root {
    --page-bg: #f4f4f4;
    --sky: #eef3f6;
    --sea: #b9d3dc;
    --sea-deep: #8fb3c1;
    --shore: #6f7a72;
    --grass: #a8c63c;
    --bubble-blue: #5bbfd0;
    --bubble-green: #a3c93a;
    --ink-light: #ffffff;
  }
  * { margin: 0; padding: 0; box-sizing: border-box; }
  html, body {
    width: 1200px;
    height: 1200px;
    overflow: hidden;
    background: var(--page-bg);
  }
  .banner {
    position: absolute;
    left: 102px;
    top: 416px;
    width: 996px;
    height: 366px;
    overflow: hidden;
  }
  .banner svg { display: block; }
  .headline { font-family: "Delius", "Comic Neue", cursive; fill: var(--ink-light); }
  .contact { font-family: "Varela Round", "Nunito", sans-serif; fill: var(--ink-light); font-size: 20px; }
</style>
</head>
<body>
  <section class="banner">
    <svg width="996" height="366" viewBox="0 0 996 366" xmlns="http://www.w3.org/2000/svg">
      <defs>
        <linearGradient id="sceneGradient" x1="0" y1="0" x2="0" y2="1">
          <stop offset="0" stop-color="#f3f6f8"/>
          <stop offset="0.22" stop-color="#dfe8ee"/>
          <stop offset="0.35" stop-color="#b6ccd5"/>
          <stop offset="0.55" stop-color="#c9dce2"/>
          <stop offset="0.68" stop-color="#e7eef0"/>
          <stop offset="0.78" stop-color="#7f8a80"/>
          <stop offset="0.88" stop-color="#a9c450"/>
          <stop offset="1" stop-color="#a6c53a"/>
        </linearGradient>
        <linearGradient id="glareGradient" x1="0" y1="0" x2="1" y2="0">
          <stop offset="0.5" stop-color="#ffffff" stop-opacity="0"/>
          <stop offset="1" stop-color="#ffffff" stop-opacity="0.75"/>
        </linearGradient>
        <filter id="softShadow" x="-10%" y="-10%" width="120%" height="130%">
          <feDropShadow dx="0" dy="1.5" stdDeviation="1.5" flood-color="#2b5560" flood-opacity="0.35"/>
        </filter>
      </defs>

      <g class="scene-photo" role="img" aria-label="Photo of a rocky Gold Coast beach with surfers in the waves, a pine branch overhead, a distant city skyline and a grassy foreground">
        <rect width="996" height="366" fill="url(#sceneGradient)"/>
        <rect width="996" height="366" fill="url(#glareGradient)"/>
      </g>

      <g class="bubble bubble-main">
        <circle cx="424" cy="160" r="127" fill="var(--bubble-blue)" opacity="0.9"/>
        <g class="headline" filter="url(#softShadow)" text-anchor="middle">
          <text x="424" y="111" font-size="54">Work</text>
          <text x="352" y="164" font-size="30">from</text>
          <text x="458" y="166" font-size="56">Home</text>
          <text x="426" y="196" font-size="22">with your</text>
          <text x="426" y="234" font-size="26">Laptop &amp; Phone</text>
        </g>
      </g>

      <g class="bubble bubble-accent">
        <circle cx="624" cy="160" r="84" fill="var(--bubble-green)" opacity="0.92"/>
        <g class="headline" filter="url(#softShadow)" text-anchor="middle">
          <text x="626" y="132" font-size="22">Create the</text>
          <text x="626" y="172" font-size="34">Lifestyle</text>
          <text x="626" y="202" font-size="16">you always wanted</text>
        </g>
      </g>

      <g class="contacts">
        <rect x="322" y="326" width="22" height="22" rx="3" fill="var(--ink-light)" opacity="0.9"/>
        <text class="contact" x="354" y="344">UpWithSun</text>
        <circle cx="477" cy="337" r="11" fill="var(--ink-light)" opacity="0.9"/>
        <text class="contact" x="496" y="344">Coraldrifthour.com</text>
      </g>
    </svg>
  </section>
</body>
</html>
```